WEBSITE DESIGN, VELTRA paint and panel

We are in need of a website for Veltra Paint & Panel based in Brisbane, Australia. We are a boutique Automotive Paint & Panel Company that provides services to all makes and models of vehicles. We have attached a logo that is still in draft stage but gives you an idea of the colour scheme and fonts and overall impact we are looking for. We are after a white background so this is clean and crisp whilst being sleek, modern and professional. The website must represent our slogan of Flawless shade on the Finest frame. The website must therefore be visually effective as our product is to get colour and placement on vehicle body's correct so the website must have this impact on our clients. We are after a widescreen webpage that is simple and logical to navigate. The final design should give clients the confidence that we can deliver on our promise.
Updates

Target Market(s)

Vehicle Owners who have a need for panel repairs and people who want to reinvigorate their car with a new coat of paint.

Industry/Entity Type

Car Repair

Coding

Coded - Design and coding required

Number of Pages Required

5+ page

Font styles to use
Sans Serif

Colors
ffffff
ffc214
000000

Requirements
Must have
• Page 1 - Home Page
• Page 2 - Our Process
• Page 3 - Private Customers
• Page 4 - Fleet & Corporate
• Page 5 - Insurance
• Page 6 - Get a Quote
• Page 7 - Connect (Contacts Page)
• Same font and colour scheme as the logo.
Should not have
• A typical mechanical/paint and panel layout which looks like a template website.

```html
<!DOCTYPE html>
<html lang="en">
<head>
<meta charset="utf-8">
<title>Veltra Paint &amp; Panel</title>
<link rel="stylesheet" href="https://fonts.googleapis.com/css2?family=Open+Sans:wght@400;600;700&family=Roboto:wght@500;700&family=Noto+Serif:wght@700&display=swap">
<style>
:root{
  --yellow:#ffc214;
  --amber:#f2a30f;
  --black:#000000;
  --white:#ffffff;
  --ink:#333333;
  --muted:#777777;
  --dark:#232323;
  --darker:#1a1a1a;
  --navy:#1f2b3a;
  --line:#e2e2e2;
  --photo-a:#3a3d42;
  --photo-b:#8a8d92;
}
*{box-sizing:border-box;margin:0;padding:0}
html,body{width:1200px;height:4588px;overflow:hidden}
body{font-family:"Open Sans",Arial,sans-serif;color:var(--ink);background:var(--white);font-size:12px;line-height:1.6;position:relative}
section,header,footer{position:absolute;left:0;width:1200px}
.section-title{position:absolute;left:0;width:1200px;text-align:center;font-family:"Roboto",Arial,sans-serif;font-weight:700;font-size:16px;color:var(--amber);letter-spacing:1px;text-transform:uppercase}
.section-title::after{content:"";display:block;width:40px;height:2px;background:var(--yellow);margin:10px auto 0}
.photo{background:linear-gradient(135deg,var(--photo-a),var(--photo-b))}

/* header */
.site-header{top:0;height:70px;background:var(--white);z-index:3;box-shadow:0 1px 4px rgba(0,0,0,.1)}
.brand{position:absolute;left:40px;top:10px;height:40px;display:flex;align-items:center;gap:10px}
.brand-mark{width:22px;height:22px;background:var(--yellow)}
.brand-name{font-family:"Roboto",Arial,sans-serif;font-weight:700;font-size:26px;color:var(--black);letter-spacing:2px}
.brand-tag{position:absolute;left:40px;top:48px;font-size:8px;color:var(--muted);letter-spacing:1px;white-space:nowrap}
.main-nav{position:absolute;left:250px;top:26px;display:flex;gap:22px;font-family:"Roboto",Arial,sans-serif;font-weight:500;font-size:12px;color:var(--ink);text-transform:uppercase;white-space:nowrap}
.main-nav .active{color:var(--amber)}
.btn-appoint{position:absolute;right:40px;top:20px;background:var(--navy);color:var(--white);font-family:"Roboto",Arial,sans-serif;font-size:11px;font-weight:700;padding:8px 16px;text-transform:uppercase}

/* hero */
.hero{top:70px;height:750px;background:linear-gradient(120deg,#1c1d20 0%,#4a4c50 45%,#2a2b2e 100%)}
.hero-sidebar{position:absolute;left:0;top:0;width:280px;height:400px;background:rgba(20,20,20,.82);color:var(--white);padding:24px 30px}
.hero-sidebar h4{font-family:"Roboto",Arial,sans-serif;font-size:14px;font-weight:700;text-transform:uppercase;display:flex;align-items:center;gap:8px;margin-bottom:10px}
.hero-sidebar .row{display:flex;justify-content:space-between;font-size:11px;color:#cfcfcf;padding-left:24px}
.hero-sidebar .block{margin-bottom:22px}
.hero-sidebar .addr{font-size:11px;color:#cfcfcf;padding-left:24px}
.hero-sidebar .mini-btn{display:inline-block;margin:8px 0 0 24px;border:1px solid #888;font-size:9px;padding:3px 10px;color:#ddd}
.hotline-num{font-family:"Roboto",Arial,sans-serif;font-size:24px;font-weight:700;padding-left:24px}
.hero-copy{position:absolute;left:600px;top:330px;width:520px;color:var(--white)}
.hero-copy h1{font-family:"Roboto",Arial,sans-serif;font-size:40px;font-weight:700;letter-spacing:1px;white-space:nowrap}
.hero-copy p{font-size:12px;color:#dcdcdc;margin-top:2px}
.hero-copy .learn{position:absolute;right:0;top:64px;background:var(--white);color:var(--black);font-size:10px;font-weight:700;padding:6px 12px;text-transform:uppercase;white-space:nowrap}

/* services */
.services{top:820px;height:480px;background:var(--white)}
.service-grid{position:absolute;left:90px;top:150px;width:1020px;display:grid;grid-template-columns:repeat(3,1fr);column-gap:40px;row-gap:60px}
.service{display:flex;gap:12px}
.service-text{flex:1}
.service h3{font-family:"Roboto",Arial,sans-serif;font-size:16px;font-weight:700;color:var(--amber);margin-bottom:6px}
.service p{font-size:11px;color:var(--muted);line-height:1.5}
.service .more{font-size:9px;color:var(--amber);margin-top:6px}
.service-thumb{width:76px;height:76px;border-radius:50%;flex:none;margin-top:20px}

/* about + specialists */
.about{top:1300px;height:540px;background:linear-gradient(90deg,#6f7276,#a6a9ad 50%,#6d7074)}
.about-panel{position:absolute;left:40px;top:40px;width:560px;height:460px;background:rgba(235,235,235,.92);padding:30px 40px}
.about-panel h2{font-family:"Roboto",Arial,sans-serif;font-size:18px;font-weight:700;color:var(--black);text-transform:uppercase;margin-bottom:14px}
.about-panel p{font-size:11px;color:#555;margin-bottom:18px}
.about-panel h5{font-size:11px;font-weight:700;text-transform:uppercase;margin-bottom:8px;color:var(--black)}
.feature-list{list-style:none;font-size:11px;color:#555}
.feature-list li{display:flex;align-items:center;gap:8px;line-height:1.9}
.feature-list li::before{content:"";width:5px;height:5px;background:var(--amber);border-radius:50%}
.specialists{position:absolute;left:610px;top:40px;width:550px;height:460px;background:var(--yellow);padding:24px 30px}
.specialists h2{font-family:"Roboto",Arial,sans-serif;font-size:18px;font-weight:700;color:var(--white);text-transform:uppercase;margin-bottom:18px}
.team-grid{display:grid;grid-template-columns:repeat(3,1fr);grid-template-rows:175px 175px;gap:10px}
.view-team{display:flex;align-items:center;justify-content:flex-end;padding-right:16px;text-align:right;background:linear-gradient(135deg,#c99a10,#e8b218);color:var(--white);font-family:"Roboto",Arial,sans-serif;font-size:26px;font-weight:700;line-height:1.05;text-transform:uppercase}

/* news */
.news{top:1840px;height:780px;background:var(--white)}
.news-grid{position:absolute;left:50px;top:200px;display:flex;gap:40px}
.news-card{width:340px;height:540px;background:var(--yellow);box-shadow:0 2px 6px rgba(0,0,0,.12)}
.news-card .photo{height:220px}
.news-body{padding:18px 22px}
.news-date{display:inline-block;background:var(--white);font-size:9px;font-weight:700;padding:2px 8px;color:var(--ink);margin-bottom:8px}
.news-card h3{font-family:"Roboto",Arial,sans-serif;font-size:17px;font-weight:700;color:var(--black);text-transform:uppercase;line-height:1.2;margin-bottom:14px}
.news-card p{font-size:11px;color:#4a3b06;line-height:1.6}
.news-card .more{font-size:10px;color:var(--black);margin-top:8px}

/* testimonials */
.testimonials{top:2660px;height:440px;background:linear-gradient(100deg,#1c2636,#34445c 55%,#1c2636)}
.testimonials .section-title{top:30px;color:var(--white)}
.quote{position:absolute;top:110px;width:470px;display:flex;gap:16px}
.quote .avatar{width:64px;height:64px;flex:none}
.quote .name{font-size:10px;color:var(--yellow);margin-bottom:10px}
.quote blockquote{font-family:"Noto Serif",Georgia,serif;font-weight:700;font-size:17px;line-height:1.45;color:var(--white)}
.dots{position:absolute;left:0;width:1200px;top:390px;display:flex;justify-content:center;gap:8px}
.dots span{width:7px;height:7px;border-radius:50%;background:rgba(255,255,255,.4)}
.dots span.on{background:var(--white)}

/* brands */
.brands{top:3100px;height:320px;background:var(--white)}
.brands .section-title{top:60px}
.brand-row{position:absolute;left:120px;top:150px;width:960px;display:flex;justify-content:space-between;align-items:center}
.partner-badge{width:150px;height:40px;background:#d9d9d9;border-radius:4px}
.partner-badge.dark{background:#2d2d2d;width:110px}

/* faq + contact */
.contact{top:3420px;height:560px;background:var(--white)}
.faq{position:absolute;left:100px;top:60px;width:490px}
.faq-item{background:var(--yellow);color:var(--white);font-size:11px;font-weight:600;padding:8px 14px;margin-bottom:6px;display:flex;justify-content:space-between}
.faq-open{border:1px solid var(--yellow);padding:14px;font-size:11px;color:#555;margin:-6px 0 8px;height:240px}
.form{position:absolute;left:615px;top:60px;width:485px}
.form p{font-size:11px;color:#555;margin-bottom:14px}
.field-row{display:flex;gap:14px;margin-bottom:12px}
.field{flex:1;height:34px;border:1px solid var(--line);font-size:11px;color:#999;padding:8px 10px;display:flex;justify-content:space-between}
.field.area{height:150px}
.captcha{display:inline-block;border:1px solid var(--line);font-size:10px;padding:6px 12px;color:#666;margin-bottom:10px}
.send{display:inline-block;border:1px solid #888;font-size:11px;font-weight:700;padding:8px 18px;color:var(--ink);text-transform:uppercase}

/* footer */
.site-footer{top:4000px;height:520px;background:var(--dark);color:#bdbdbd}
.foot-col{position:absolute;top:60px}
.foot-col h4{font-family:"Roboto",Arial,sans-serif;font-size:13px;font-weight:700;color:var(--white);text-transform:uppercase;margin-bottom:16px}
.foot-col p{font-size:11px;line-height:1.7;margin-bottom:16px}
.addr-table{font-size:11px;border-collapse:collapse}
.addr-table td{padding:2px 0;vertical-align:top}
.addr-table td:first-child{color:var(--white);font-weight:700;width:90px}
.post{display:flex;gap:12px;margin-bottom:18px}
.post .thumb{width:56px;height:44px;flex:none}
.post .cat{font-size:9px;color:var(--yellow)}
.post .ttl{font-family:"Roboto",Arial,sans-serif;font-size:13px;font-weight:700;color:var(--white);text-transform:uppercase;line-height:1.25}
.bottom-bar{position:absolute;left:0;width:1200px;top:4520px;height:68px;background:var(--darker);color:#8a8a8a;font-size:10px}
.bottom-bar .credit{position:absolute;left:40px;top:26px}
.socials{position:absolute;right:40px;top:24px;display:flex;gap:12px}
.socials span{width:16px;height:16px;border-radius:50%;background:#555}
</style>
</head>
<body>

<header class="site-header">
  <div class="brand"><span class="brand-mark"></span><span class="brand-name">VELTRA</span></div>
  <div class="brand-tag">Flawless shade on the Finest frame</div>
  <nav class="main-nav">
    <span class="active">Home</span><span>Our Process</span><span>Private Customers</span><span>Fleet &amp; Corporate</span><span>Insurance</span><span>Get a Quote</span><span>Connect</span>
  </nav>
  <div class="btn-appoint">Make an Appointment</div>
</header>

<section class="hero" role="img" aria-label="Close-up photograph of a freshly painted car body">
  <aside class="hero-sidebar">
    <div class="block">
      <h4><svg width="16" height="16" viewBox="0 0 16 16"><circle cx="8" cy="8" r="6.5" fill="none" stroke="#ffc214" stroke-width="1.6"/><path d="M8 4v4l3 2" stroke="#ffc214" stroke-width="1.6" fill="none"/></svg>Working Time</h4>
      <div class="row"><span>Monday - Friday</span><span>08.00 - 17.00</span></div>
      <div class="row"><span>Saturday</span><span>09.00 - 13.00</span></div>
      <div class="row"><span>Sunday</span><span>Closed</span></div>
    </div>
    <div class="block">
      <h4><svg width="16" height="16" viewBox="0 0 16 16"><path d="M8 15s5-5.5 5-9A5 5 0 0 0 3 6c0 3.5 5 9 5 9z" fill="#ffc214"/><circle cx="8" cy="6" r="2" fill="#141414"/></svg>Location</h4>
      <div class="addr">48 Corvel Street, Albion QLD<br>Brisbane, Australia</div>
      <span class="mini-btn">View Map</span>
    </div>
    <div class="block">
      <h4><svg width="16" height="16" viewBox="0 0 16 16"><path d="M4 1.5l2.5 3-1.5 2a8 8 0 0 0 4.5 4.5l2-1.5 3 2.5-1.5 2.5C7 14.5 1.5 9 1.5 3z" fill="#ffc214"/></svg>24 Hours Hotline</h4>
      <div class="hotline-num">07 3100 4821</div>
      <div class="addr">Mobile: 0412 558 907</div>
    </div>
  </aside>
  <div class="hero-copy">
    <h1>Flawless Shade, Finest Frame</h1>
    <p>Careful panel repair and paint matched to the factory colour of your car</p>
    <span class="learn">Get a Quote</span>
  </div>
</section>

<section class="services">
  <h2 class="section-title" style="top:100px">Our Service</h2>
  <div class="service-grid">
    <div class="service"><div class="service-text"><h3>Body Repair &amp; Paint</h3><p>Dents, scratches and crash damage put right, then painted to match every panel.</p><div class="more">View details</div></div><div class="service-thumb photo" role="img" aria-label="Photo of a car body panel"></div></div>
    <div class="service"><div class="service-text"><h3>Colour Matching</h3><p>Every shade measured and mixed in house so new paint blends with the old.</p><div class="more">View details</div></div><div class="service-thumb photo" role="img" aria-label="Photo of paint swatches"></div></div>
    <div class="service"><div class="service-text"><h3>Insurance Repairs</h3><p>We deal with your insurer directly and keep you posted at every step.</p><div class="more">View details</div></div><div class="service-thumb photo" role="img" aria-label="Photo of a damaged car door"></div></div>
    <div class="service"><div class="service-text"><h3>Full Resprays</h3><p>Complete resprays in any shade with a deep gloss and an even, lasting coat.</p><div class="more">View details</div></div><div class="service-thumb photo" role="img" aria-label="Photo of a spray gun"></div></div>
    <div class="service"><div class="service-text"><h3>Bumper Repair</h3><p>Bumpers and trims repaired, fitted and blended into the original colour.</p><div class="more">View details</div></div><div class="service-thumb photo" role="img" aria-label="Photo of a car bumper"></div></div>
    <div class="service"><div class="service-text"><h3>Fleet Care</h3><p>Fast, planned repairs for business fleets to keep vehicles on the road.</p><div class="more">View details</div></div><div class="service-thumb photo" role="img" aria-label="Photo of company vans"></div></div>
  </div>
</section>

<section class="about" role="img" aria-label="Photograph of a paint booth interior">
  <div class="about-panel">
    <h2>About Veltra Paint &amp; Panel</h2>
    <p>Veltra Paint &amp; Panel is a boutique workshop in Brisbane looking after all makes and models. Our team matches colour by eye and by measure, so every repair sits flush and shines like the rest of the car. We treat each vehicle as if it were our own.</p>
    <h5>Why Choose Us</h5>
    <ul class="feature-list">
      <li>Lifetime warranty on paint work</li>
      <li>Computer colour matching for every make, model and finish</li>
      <li>Free insurance quotes</li>
      <li>Courtesy cars on request</li>
      <li>Dust-free heated spray booth</li>
      <li>Fleet and corporate accounts</li>
      <li>Photo updates during repair</li>
      <li>Pick-up and drop-off service</li>
    </ul>
  </div>
  <div class="specialists">
    <h2>Our Specialists</h2>
    <div class="team-grid">
      <div class="photo" role="img" aria-label="Photo of a team member"></div>
      <div class="photo" role="img" aria-label="Photo of a team member"></div>
      <div class="photo" role="img" aria-label="Photo of a team member"></div>
      <div class="photo" role="img" aria-label="Photo of a team member"></div>
      <div class="photo" role="img" aria-label="Photo of a team member"></div>
      <div class="view-team">View<br>Team</div>
    </div>
  </div>
</section>

<section class="news">
  <h2 class="section-title" style="top:110px">Latest News</h2>
  <div class="news-grid">
    <article class="news-card"><div class="photo" role="img" aria-label="Photo of a painter at work"></div><div class="news-body"><span class="news-date">May 17, 2024</span><h3>How We Match Metallic Paint Perfectly</h3><p>Metallic and pearl finishes change with light and angle. Our painters use a spectrometer, test cards and daylight lamps to mix a shade that disappears into the panels around it, then blend the edges so no line is ever seen once your car is back in the sun.</p><div class="more">Read more</div></div></article>
    <article class="news-card"><div class="photo" role="img" aria-label="Photo of a technician beside a car"></div><div class="news-body"><span class="news-date">May 17, 2024</span><h3>What to Do After a Minor Collision</h3><p>Take photos, swap details and call your insurer. Then bring the car to us for a free assessment. We will check the hidden damage behind the panel, explain the options clearly and handle the claim paperwork, so you can get back on the road quickly.</p><div class="more">Read more</div></div></article>
    <article class="news-card"><div class="photo" role="img" aria-label="Photo of a team inspecting a car"></div><div class="news-body"><span class="news-date">May 17, 2024</span><h3>Caring for New Paint in the First Month</h3><p>Fresh paint needs time to cure. Wash by hand with mild soap, avoid automatic car washes and skip waxing for four weeks. Park in the shade where you can, and rinse off bird droppings quickly so your new finish stays deep, even and glossy for years.</p><div class="more">Read more</div></div></article>
  </div>
</section>

<section class="testimonials" role="img" aria-label="Dim photograph of a car in a workshop">
  <h2 class="section-title">What They Say About Us</h2>
  <div class="quote" style="left:80px"><div class="avatar photo" role="img" aria-label="Customer portrait"></div><div><div class="name">Mara Quinlan, Fleet Manager</div><blockquote>Veltra looks after our whole fleet. Repairs are quick, quotes are clear and every van comes back with paint you could never tell apart from the factory finish. Our drivers are back on the road sooner and the vehicles look better than ever before.</blockquote></div></div>
  <div class="quote" style="left:640px"><div class="avatar photo" role="img" aria-label="Customer portrait"></div><div><div class="name">Tobin Aldous, Engineer</div><blockquote>After a car park scrape I expected a patchy repair. Instead the door matches the rest of the car exactly, even in bright sun. The team kept me updated with photos and handled the insurance claim from start to finish without any fuss at all.</blockquote></div></div>
  <div class="dots"><span class="on"></span><span></span></div>
</section>

<section class="brands">
  <h2 class="section-title">Brand Partner</h2>
  <div class="brand-row">
    <div class="partner-badge" role="img" aria-label="Partner badge"></div>
    <div class="partner-badge" role="img" aria-label="Partner badge"></div>
    <div class="partner-badge" role="img" aria-label="Partner badge"></div>
    <div class="partner-badge dark" role="img" aria-label="Partner badge"></div>
  </div>
</section>

<section class="contact">
  <div class="faq">
    <div class="faq-item"><span>How long does a standard panel repair take?</span><span>&minus;</span></div>
    <div class="faq-open">Most panel repairs take between two and five working days, depending on the damage and the paint system. We give you a firm date at the quote stage and keep you updated by phone or text while your car is with us. Larger insurance jobs may take longer where parts must be ordered in, and we will always tell you before work begins. Courtesy cars can be arranged on request.</div>
    <div class="faq-item"><span>Do you work with all insurance companies?</span><span>+</span></div>
    <div class="faq-item"><span>Can you match metallic and pearl colours?</span><span>+</span></div>
    <div class="faq-item"><span>Do you offer a warranty on paint work?</span><span>+</span></div>
    <div class="faq-item"><span>How do I book my car in for a quote?</span><span>+</span></div>
  </div>
  <div class="form">
    <p>Send us a few details about your car and the work you need, and our team will reply with a quote within one business day.</p>
    <div class="field-row"><div class="field">Name</div><div class="field">Email</div></div>
    <div class="field-row"><div class="field">Phone</div><div class="field"><span>Service type</span><span>&#9662;</span></div></div>
    <div class="field-row"><div class="field area">Type your message here</div></div>
    <div class="captcha">Attach Photos</div><br>
    <span class="send">Send This Message</span>
  </div>
</section>

<footer class="site-footer">
  <div class="foot-col" style="left:40px;width:320px">
    <h4>About Us</h4>
    <p>Veltra Paint &amp; Panel is a boutique body shop caring for every make and model. We repair, refinish and protect, so your car leaves looking as good as the day it was built.</p>
    <p>Our painters match each shade under daylight lamps and check every panel twice. Fair prices, clear quotes and honest advice are part of every job we take on.</p>
  </div>
  <div class="foot-col" style="left:420px;width:330px">
    <h4>Office Address</h4>
    <table class="addr-table">
      <tr><td>Location</td><td>48 Corvel Street, Albion QLD 4010, Brisbane</td></tr>
      <tr><td>Telp</td><td>07 3100 4821</td></tr>
      <tr><td>Email</td><td>hello@veltrapanel.au</td></tr>
      <tr><td>Open Hours</td><td>Monday - Friday<br>08.00 - 17.00</td></tr>
    </table>
    <p style="margin:14px 0 6px">Second Office</p>
    <table class="addr-table">
      <tr><td>Location</td><td>12 Harlow Lane, Eagle Farm QLD 4009</td></tr>
      <tr><td>Telp</td><td>07 3100 4822</td></tr>
      <tr><td>Email</td><td>fleet@veltrapanel.au</td></tr>
      <tr><td>Open Hours</td><td>Monday - Friday<br>08.00 - 17.00</td></tr>
    </table>
  </div>
  <div class="foot-col" style="left:820px;width:340px">
    <h4>Latest Posts</h4>
    <div class="post"><div class="thumb photo" role="img" aria-label="Post thumbnail"></div><div><div class="cat">Paint Tips</div><div class="ttl">How We Match Metallic Paint Perfectly</div></div></div>
    <div class="post"><div class="thumb photo" role="img" aria-label="Post thumbnail"></div><div><div class="cat">Insurance, Advice</div><div class="ttl">What to Do After a Minor Collision</div></div></div>
    <div class="post"><div class="thumb photo" role="img" aria-label="Post thumbnail"></div><div><div class="cat">Paint Tips</div><div class="ttl">Caring for New Paint in the First Month</div></div></div>
  </div>
</footer>

<div class="bottom-bar">
  <span class="credit">Powered by Veltra Studio &middot; Built by Veltra</span>
  <div class="socials"><span></span><span></span><span></span><span></span><span></span><span></span><span></span></div>
</div>

</body>
</html>
```